Wendlin Storen
Zielgruppe
Storenbau: Lammellenstoren, Markisen, Beschattungen, Klappläden
Service: Reparatur und Unterhalt bestehender Anlagen
Aufgabenstellung
Klare Linen / wenig Schnörkel
Briefpapier: ein schwacher, Wasserzeichen-ähnlicher Schriftzug seitlich/unten am rechten Rand würde uns gefallen...
Die Farbe Azurblau RAL5009 (oder ähnlich) haben wir in Erwägung gezogen ...

```html
<!DOCTYPE html>
<html lang="de">
<head>
<meta charset="utf-8">
<title>Wendlin Storenbau GmbH – Geschäftsausstattung</title>
<link href="https://fonts.googleapis.com/css2?family=Open+Sans:wght@300;400;600&display=swap" rel="stylesheet">
<style>
  :root{
    --azure:#0a5a92;
    --slate:#545b60;
    --paper:#ffffff;
    --ground:#e8e5e1;
    --rule:#d9dbdd;
    --window:#ebebeb;
    --text-soft:#7a8085;
  }
  *{margin:0;padding:0;box-sizing:border-box}
  html,body{width:779px;height:1200px;overflow:hidden}
  body{background:var(--ground);font-family:"Open Sans",sans-serif;color:var(--slate);position:relative}
  .sheet{position:absolute;background:var(--paper)}
  .wordmark{position:absolute;font-weight:600;line-height:1;white-space:nowrap;text-align:center}
  .wordmark .name{display:block;letter-spacing:-.02em}
  .wordmark .legal{display:block;letter-spacing:.6em;margin-top:.25em;font-size:.45em;padding-left:.6em}

  /* Letterhead */
  .letterhead{left:9px;top:28px;width:512px;height:725px}
  .letterhead .wordmark{left:60px;top:38px;font-size:21px;color:var(--azure)}
  .sender-line{position:absolute;left:60px;top:118px;width:178px;font-size:6px;font-weight:300;padding-bottom:4px;border-bottom:.6px solid var(--rule);white-space:nowrap}
  .sender-line b{font-weight:400}
  .fold-mark{position:absolute;left:0;width:15px;height:.8px;background:var(--rule)}
  .footer-rule{position:absolute;left:63px;top:656px;width:380px;height:.8px;background:var(--rule)}
  .footer{position:absolute;top:670px;left:63px;width:390px;font-size:5.6px;font-weight:300;line-height:9.4px}
  .footer .col{position:absolute;top:0;white-space:nowrap}
  .caps{font-weight:400;text-transform:uppercase}
  .icon{position:absolute;width:7px;height:7px}
  .ico-row{position:relative;padding-left:14px}
  .ico-row svg{position:absolute;left:0;top:1px}

  /* Cards */
  .card{left:547px;width:207px;height:134px}
  .card-front{top:28px}
  .card-front .wordmark{left:11px;top:14px;font-size:11.5px;color:var(--azure);text-align:left}
  .card-front .wordmark .legal{text-align:center}
  .person{position:absolute;right:13px;top:50px;text-align:right}
  .person .person-name{font-size:12px;font-weight:300;letter-spacing:.03em}
  .person .role{font-size:5.6px;font-weight:300;letter-spacing:.3em;margin-top:2px}
  .card-contact{position:absolute;top:86px;font-size:5.4px;font-weight:300;line-height:10px;white-space:nowrap}
  .card-contact.left{left:12px}
  .card-contact.right{left:105px}
  .card-back{top:176px}
  .card-azure{top:323px;background:var(--azure)}
  .card-slate{top:471px;background:var(--slate)}
  .card-back .wordmark,.card-azure .wordmark,.card-slate .wordmark{left:0;right:0;top:53px;font-size:17px}
  .card-back .wordmark{color:var(--azure)}
  .card-azure .wordmark,.card-slate .wordmark{color:#fff}

  /* Envelope */
  .envelope{left:12px;top:768px;width:558px;height:394px}
  .envelope .wordmark{left:28px;top:37px;font-size:17px;color:var(--azure)}
  .address-window{position:absolute;left:50px;top:139px;width:243px;height:109px;border-radius:9px;background:var(--window)}
</style>
</head>
<body>

<section class="sheet letterhead" aria-label="Briefpapier">
  <div class="wordmark"><span class="name">Wendlin Storenbau</span><span class="legal">GmbH</span></div>
  <p class="sender-line"><b>WENDLIN STORENBAU GMBH</b> · 14 Seeweg · 8048 Zürich</p>
  <span class="fold-mark" style="top:257px"></span>
  <span class="fold-mark" style="top:362px"></span>
  <span class="fold-mark" style="top:513px"></span>
  <div class="footer-rule"></div>
  <div class="footer">
    <div class="col ico-row" style="left:0">
      <svg class="icon" viewBox="0 0 10 10"><path d="M5 9.5C2.5 6.5 1.8 5 1.8 3.8a3.2 3.2 0 0 1 6.4 0C8.2 5 7.5 6.5 5 9.5z" fill="none" stroke="var(--azure)" stroke-width="1.2"/><circle cx="5" cy="3.8" r="1" fill="var(--azure)"/></svg>
      <span class="caps">Wendlin Storenbau</span><br><span class="caps">GmbH</span><br>14 Seeweg<br>8048 Zürich
    </div>
    <div class="col" style="left:96px">
      <div class="ico-row"><svg class="icon" viewBox="0 0 10 10"><circle cx="5" cy="5" r="4.2" fill="none" stroke="var(--azure)" stroke-width="1"/><path d="M3.5 3c.3 2 1.5 3.3 3.3 3.7l.4-1" fill="none" stroke="var(--azure)" stroke-width="1"/></svg>+41 44 555 12 30</div>
      <div class="ico-row"><svg class="icon" viewBox="0 0 10 10"><rect x="1" y="3" width="8" height="6.2" fill="none" stroke="var(--azure)" stroke-width="1"/><rect x="3" y=".8" width="4" height="3" fill="none" stroke="var(--azure)" stroke-width="1"/></svg>+41 44 555 12 31</div>
      <div class="ico-row"><svg class="icon" viewBox="0 0 10 10"><rect x=".8" y="2" width="8.4" height="6" fill="none" stroke="var(--azure)" stroke-width="1"/><path d="M.8 2L5 5.5 9.2 2" fill="none" stroke="var(--azure)" stroke-width="1"/></svg>info@wendlin-storenbau.ch</div>
      <div class="ico-row"><svg class="icon" viewBox="0 0 10 10"><circle cx="5" cy="5" r="4.2" fill="none" stroke="var(--azure)" stroke-width="1"/><ellipse cx="5" cy="5" rx="1.8" ry="4.2" fill="none" stroke="var(--azure)" stroke-width=".8"/><path d="M.8 5h8.4" stroke="var(--azure)" stroke-width=".8"/></svg>www.wendlin-storenbau.ch</div>
    </div>
    <div class="col" style="left:218px">Handelsregister Zürich<br>USt.-Id.-Nr. CHxxxxxxx<br>St.-Nr. xx/xxx/xxxx/x</div>
    <div class="col" style="left:302px">Bank Name: xxxxxxxxxxxx<br>IBAN: CH xxxx xxxx xxxx xxxx xx<br>BIC: xxxxxxxxx</div>
  </div>
</section>

<section class="sheet card card-front" aria-label="Visitenkarte Vorderseite">
  <div class="wordmark"><span class="name">Wendlin Storenbau</span><span class="legal">GmbH</span></div>
  <div class="person"><p class="person-name">NINA KESSMAR</p><p class="role">EXECUTIVE MANAGER</p></div>
  <div class="card-contact left ico-row">
    <svg class="icon" viewBox="0 0 10 10"><path d="M5 9.5C2.5 6.5 1.8 5 1.8 3.8a3.2 3.2 0 0 1 6.4 0C8.2 5 7.5 6.5 5 9.5z" fill="none" stroke="var(--azure)" stroke-width="1.2"/><circle cx="5" cy="3.8" r="1" fill="var(--azure)"/></svg>
    <span class="caps">Wendlin Storenbau</span><br><span class="caps">GmbH</span><br>14 Seeweg<br>8048 Zürich
  </div>
  <div class="card-contact right">
    <div class="ico-row"><svg class="icon" viewBox="0 0 10 10"><circle cx="5" cy="5" r="4.2" fill="none" stroke="var(--azure)" stroke-width="1"/><path d="M3.5 3c.3 2 1.5 3.3 3.3 3.7l.4-1" fill="none" stroke="var(--azure)" stroke-width="1"/></svg>+41 44 555 12 30</div>
    <div class="ico-row"><svg class="icon" viewBox="0 0 10 10"><rect x="1" y="3" width="8" height="6.2" fill="none" stroke="var(--azure)" stroke-width="1"/><rect x="3" y=".8" width="4" height="3" fill="none" stroke="var(--azure)" stroke-width="1"/></svg>+41 44 555 12 31</div>
    <div class="ico-row"><svg class="icon" viewBox="0 0 10 10"><rect x=".8" y="2" width="8.4" height="6" fill="none" stroke="var(--azure)" stroke-width="1"/><path d="M.8 2L5 5.5 9.2 2" fill="none" stroke="var(--azure)" stroke-width="1"/></svg>info@wendlin-storenbau.ch</div>
    <div class="ico-row"><svg class="icon" viewBox="0 0 10 10"><circle cx="5" cy="5" r="4.2" fill="none" stroke="var(--azure)" stroke-width="1"/><ellipse cx="5" cy="5" rx="1.8" ry="4.2" fill="none" stroke="var(--azure)" stroke-width=".8"/><path d="M.8 5h8.4" stroke="var(--azure)" stroke-width=".8"/></svg>www.wendlin-storenbau.ch</div>
  </div>
</section>

<section class="sheet card card-back" aria-label="Visitenkarte Rückseite weiss">
  <div class="wordmark"><span class="name">Wendlin Storenbau</span><span class="legal">GmbH</span></div>
</section>

<section class="sheet card card-azure" aria-label="Visitenkarte Rückseite azurblau">
  <div class="wordmark"><span class="name">Wendlin Storenbau</span><span class="legal">GmbH</span></div>
</section>

<section class="sheet card card-slate" aria-label="Visitenkarte Rückseite grau">
  <div class="wordmark"><span class="name">Wendlin Storenbau</span><span class="legal">GmbH</span></div>
</section>

<section class="sheet envelope" aria-label="Briefumschlag">
  <div class="wordmark"><span class="name">Wendlin Storenbau</span><span class="legal">GmbH</span></div>
  <div class="address-window"></div>
</section>

</body>
</html>
```